Flyer Re-Design

We need a flyer re-design for a company that recently started doing it's own graphic design. Although we've taken a first attempt at the design, we would like a design professional, like yourself show us how much better you can do it. We're going through a re-branding as the logo reads "formerly" known as and although we'd like to keep the logo as it is---everything else should be more contemporary.

5.5" x 8.5" or 5" x 7"

Target Market(s)

Bahamas Youth

Industry/Entity Type

Graphic Design

Font styles to use
Sans Serif

Requirements
Must have
• Current Logo. Include as many details as already listed in the document.
Nice to have
• Fresh New, Crisp Ideas for this Pharmacy rebranding
Should not have
• Too Many colors or serif fonts

```html
<!DOCTYPE html>
<html lang="en">
<head>
<meta charset="utf-8">
<title>Vital Grove Pharmacy – Rewards Club Flyer</title>
<link href="https://fonts.googleapis.com/css2?family=Poppins:wght@400;500;600;700;800&display=swap" rel="stylesheet">
<style>
  :root {
    --red: #c8232c;
    --red-dark: #a3161e;
    --green: #1f9d55;
    --green-dark: #17703c;
    --green-soft: #e9f5ec;
    --mist: #f4f9f1;
    --panel: #f1f2f1;
    --ink: #1b1f1d;
    --muted: #5b625e;
    --white: #ffffff;
  }
  * { box-sizing: border-box; margin: 0; padding: 0; }
  html, body { width: 858px; height: 1200px; overflow: hidden; background: var(--white); }
  .flyer {
    position: relative; width: 858px; height: 1200px; overflow: hidden;
    font-family: "Poppins", Arial, sans-serif; color: var(--ink);
    background: linear-gradient(180deg, var(--white) 0%, var(--mist) 60%, var(--white) 100%);
  }

  /* Brand header */
  .brand { position: absolute; left: 48px; top: 38px; width: 762px; height: 110px; }
  .brand-mark {
    position: absolute; left: 0; top: 4px; width: 100px; height: 100px;
    border-radius: 50%; background: var(--green);
  }
  .brand-name {
    position: absolute; left: 130px; top: 14px;
    font-weight: 600; font-size: 32px; letter-spacing: 2px; line-height: 1.2;
    text-transform: uppercase; color: var(--red); white-space: nowrap;
  }
  .brand-rule {
    position: absolute; left: 132px; top: 62px; width: 620px; height: 3px;
    background: var(--green); border-radius: 2px;
  }
  .brand-tagline {
    position: absolute; left: 132px; top: 76px;
    font-weight: 500; font-size: 16px; letter-spacing: 4px; line-height: 1.2;
    text-transform: uppercase; color: var(--green-dark); white-space: nowrap;
  }

  /* Headline band */
  .headline-band {
    position: absolute; left: 0; top: 186px; width: 720px; height: 96px;
    background: var(--red); border-radius: 0 48px 48px 0;
  }
  .headline {
    position: absolute; left: 48px; top: 186px; height: 96px;
    display: flex; align-items: center; gap: 14px;
    color: var(--white); font-weight: 800; font-size: 58px; line-height: 1;
    letter-spacing: -0.5px; white-space: nowrap;
  }
  .headline .light { font-weight: 400; font-size: 40px; letter-spacing: 0; }

  /* Hero photo area */
  .hero-photo {
    position: absolute; right: 0; top: 306px; width: 310px; height: 372px;
    border-radius: 28px 0 0 28px;
    background: radial-gradient(ellipse at 60% 38%, #f2d6c2 0%, #e8cda4 32%, #a9cde4 70%, #d6ebf5 100%);
  }

  /* Benefits */
  .benefits {
    position: absolute; left: 48px; top: 306px; width: 478px;
    list-style: none; display: flex; flex-direction: column; gap: 14px;
  }
  .benefit {
    display: flex; align-items: center; gap: 16px;
    min-height: 70px; padding: 12px 20px;
    background: var(--green); color: var(--white);
    border-radius: 14px; font-size: 18px; font-weight: 500; line-height: 1.3;
  }
  .benefit-dot {
    flex: none; width: 34px; height: 34px; border-radius: 50%;
    background: var(--white); display: flex; align-items: center; justify-content: center;
  }

  .thanks {
    position: absolute; left: 0; top: 702px; width: 858px; text-align: center;
    font-weight: 700; font-size: 32px; line-height: 1.2; color: var(--red); white-space: nowrap;
  }
  .thanks .accent { color: var(--green-dark); }

  /* Exclusives */
  .exclusives {
    position: absolute; left: 48px; top: 772px; width: 762px; height: 262px;
    background: var(--panel); border-radius: 24px;
  }
  .exclusives-tag {
    position: absolute; left: 50%; top: -22px; transform: translateX(-50%);
    padding: 0 34px; height: 46px; line-height: 46px;
    background: var(--red); color: var(--white); border-radius: 23px;
    font-weight: 700; font-size: 24px; letter-spacing: 1px; text-transform: uppercase; white-space: nowrap;
  }
  .exclusives-list {
    position: absolute; left: 48px; top: 42px; list-style: none;
    display: flex; flex-direction: column; gap: 8px;
  }
  .exclusives-list li {
    display: flex; align-items: center; gap: 18px;
    font-size: 22px; font-weight: 400; line-height: 34px; color: var(--ink); white-space: nowrap;
  }
  .tick {
    flex: none; width: 30px; height: 30px; border-radius: 50%;
    background: var(--green); display: flex; align-items: center; justify-content: center;
  }

  .cta {
    position: absolute; left: 0; top: 1054px; width: 858px; text-align: center;
    font-weight: 600; font-size: 27px; line-height: 1.2; color: var(--ink);
  }
  .footer {
    position: absolute; left: 0; top: 1118px; width: 858px; height: 82px;
    background: var(--red); color: var(--white);
    font-weight: 500; font-size: 32px; letter-spacing: 0.5px; text-align: center; line-height: 82px;
  }
</style>
</head>
<body>
<main class="flyer">
  <header class="brand">
    <div class="brand-mark"></div>
    <div class="brand-name">Vital Grove Pharmacy</div>
    <div class="brand-rule"></div>
    <div class="brand-tagline">Your Health Is Our Priority</div>
  </header>

  <div class="headline-band"></div>
  <h1 class="headline"><span>Join</span><span class="light">our</span><span>Rewards</span><span class="light">club</span></h1>

  <div class="hero-photo" role="img" aria-label="Photo of a smiling woman holding up a rewards club membership card"></div>

  <ul class="benefits">
    <li class="benefit"><span class="benefit-dot"><svg width="18" height="16" viewBox="0 0 18 16"><path d="M1 8.5 L6.5 14 L17 2" fill="none" stroke="var(--green)" stroke-width="3" stroke-linecap="round" stroke-linejoin="round"/></svg></span>Absolutely free to join!</li>
    <li class="benefit"><span class="benefit-dot"><svg width="18" height="16" viewBox="0 0 18 16"><path d="M1 8.5 L6.5 14 L17 2" fill="none" stroke="var(--green)" stroke-width="3" stroke-linecap="round" stroke-linejoin="round"/></svg></span>You’ll earn 1 point for every dollar you spend</li>
    <li class="benefit"><span class="benefit-dot"><svg width="18" height="16" viewBox="0 0 18 16"><path d="M1 8.5 L6.5 14 L17 2" fill="none" stroke="var(--green)" stroke-width="3" stroke-linecap="round" stroke-linejoin="round"/></svg></span>Earn double points on select items purchased</li>
    <li class="benefit"><span class="benefit-dot"><svg width="18" height="16" viewBox="0 0 18 16"><path d="M1 8.5 L6.5 14 L17 2" fill="none" stroke="var(--green)" stroke-width="3" stroke-linecap="round" stroke-linejoin="round"/></svg></span>Earn 25 points when you refer a friend</li>
  </ul>

  <p class="thanks">It’s just our way of saying <span class="accent">thank you.</span></p>

  <section class="exclusives">
    <h2 class="exclusives-tag">Exclusives</h2>
    <ul class="exclusives-list">
      <li><span class="tick"><svg width="16" height="14" viewBox="0 0 18 16"><path d="M1 8.5 L6.5 14 L17 2" fill="none" stroke="var(--white)" stroke-width="3" stroke-linecap="round" stroke-linejoin="round"/></svg></span>VIP access to our special events</li>
      <li><span class="tick"><svg width="16" height="14" viewBox="0 0 18 16"><path d="M1 8.5 L6.5 14 L17 2" fill="none" stroke="var(--white)" stroke-width="3" stroke-linecap="round" stroke-linejoin="round"/></svg></span>Be the first to know about our specials</li>
      <li><span class="tick"><svg width="16" height="14" viewBox="0 0 18 16"><path d="M1 8.5 L6.5 14 L17 2" fill="none" stroke="var(--white)" stroke-width="3" stroke-linecap="round" stroke-linejoin="round"/></svg></span>Free subscription to our online newsletter</li>
      <li><span class="tick"><svg width="16" height="14" viewBox="0 0 18 16"><path d="M1 8.5 L6.5 14 L17 2" fill="none" stroke="var(--white)" stroke-width="3" stroke-linecap="round" stroke-linejoin="round"/></svg></span>Free gift with sign up</li>
      <li><span class="tick"><svg width="16" height="14" viewBox="0 0 18 16"><path d="M1 8.5 L6.5 14 L17 2" fill="none" stroke="var(--white)" stroke-width="3" stroke-linecap="round" stroke-linejoin="round"/></svg></span>Special “members only” shopping events</li>
    </ul>
  </section>

  <p class="cta">See our Customer Service Representative today!</p>
  <footer class="footer">www.vitalgrovepharmacy.com</footer>
</main>
</body>
</html>
```